WordPress Design for both website and landing page for an expert

I need a clean and stylish design for my new website. I work as an expert (see attached file WHY HOW WHAT), my product is expert opinion (reports) for company evaluations You can use all of the attached pictures colored or black / white. The person is me, you can add other pictures, if you want. The design should be clean and stylish, so you could use white, black, gray, silver and / or one additional color. I have added an idea about my website, see attached file CONCEPT WEBSITE If you have any more information, please do not hesitate to contact us 'Hesitate to ask me ...

```html
<!DOCTYPE html>
<html lang="de">
<head>
<meta charset="utf-8">
<title>Lukas Renner – Sachverständiger für Firmenbewertungen</title>
<link rel="stylesheet" href="https://fonts.googleapis.com/css2?family=Jost:wght@400;500;600;700&family=Lato:wght@400;700&family=Fira+Sans:wght@500&display=swap">
<style>
  :root{
    --white:#ffffff;
    --ink:#111111;
    --grey-dark:#5f5f5f;
    --grey-text:#555555;
    --grey-soft:#777777;
    --grey-mark:#b0b7bd;
    --grey-pill:#efefef;
    --grey-line:#d4d4d4;
    --navy:#1c3354;
    --footer:#3b3b3b;
  }
  *{margin:0;padding:0;box-sizing:border-box}
  html,body{width:1200px;height:2324px;overflow:hidden;background:var(--white)}
  body{position:relative;font-family:"Lato",sans-serif;color:var(--grey-text)}
  .abs{position:absolute}

  /* hero */
  .hero{left:0;top:0;width:1200px;height:675px;
    background:
      radial-gradient(ellipse 500px 160px at 1000px 430px, rgba(240,170,80,.45), transparent 70%),
      radial-gradient(ellipse 300px 90px at 520px 360px, rgba(230,170,90,.25), transparent 70%),
      linear-gradient(180deg,#0d3f66 0%,#2a6a95 30%,#4d85a8 48%,#2a4f6c 58%,#1c5d86 72%,#163d55 88%,#1d3a2c 100%);}
  .brand{left:120px;top:88px;font-family:"Jost",sans-serif;font-weight:400;font-size:22px;letter-spacing:4px;color:var(--white)}
  .nav{left:516px;top:64px;display:flex;gap:0;font-family:"Jost",sans-serif;font-size:14px;color:var(--white)}
  .nav a{color:var(--white);text-decoration:none;position:absolute;white-space:nowrap}
  .nav .active{font-weight:700}
  .nav .active::after{content:"";position:absolute;left:0;top:21px;width:22px;height:3px;background:var(--white);transform:skewX(-30deg)}
  .hero-pill{left:194px;top:314px;width:811px;height:137px;border:1px solid rgba(255,255,255,.55);border-radius:70px;background:rgba(60,70,80,.35);text-align:center;color:var(--white)}
  .hero-title{margin-top:24px;font-family:"Fira Sans",sans-serif;font-weight:500;font-size:36px}
  .hero-sub{margin-top:4px;font-family:"Jost",sans-serif;font-size:19px}

  /* reasons */
  .mini-mark{left:582px;top:758px;width:36px;height:36px;background:#e6e6e6;border-radius:50%}
  .section-title{left:0;top:812px;width:1200px;text-align:center;font-family:"Jost",sans-serif;font-weight:600;font-size:34px;letter-spacing:1.5px;color:var(--grey-dark)}
  .reason{top:923px;width:300px;text-align:center}
  .reason svg{display:block;margin:0 auto}
  .reason h3{margin-top:34px;font-family:"Jost",sans-serif;font-weight:500;font-size:28px;color:var(--grey-dark)}
  .reason p{margin-top:10px;font-size:13.5px;line-height:22px;color:var(--ink)}

  /* promise */
  .promise{left:0;top:1298px;width:1200px;height:487px;
    background:linear-gradient(90deg,#cfcfcd 0%,#d6d5d2 45%,#c9c3bd 62%,#e3ddd6 78%,#d4a089 92%,#c9bdb3 100%)}
  .promise-text{left:100px;top:1536px;width:486px;text-align:center}
  .promise-text h2{font-family:"Jost",sans-serif;font-weight:700;font-size:33px;color:var(--ink);letter-spacing:.5px}
  .promise-text p{margin-top:8px;font-size:22px;line-height:41px;color:var(--ink)}

  /* questions */
  .divider{left:599px;top:1858px;width:1px;height:154px;background:var(--grey-line)}
  .questions{list-style:none;width:440px}
  .questions li{position:relative;padding-left:37px;font-size:15px;line-height:21px;color:var(--navy);margin-bottom:21px}
  .questions li::before{content:"";position:absolute;left:2px;top:5px;width:11px;height:11px;background:#d8dadd}

  /* call to action */
  .cta{left:127px;top:2075px;width:946px;height:76px;border:1px solid #dcdcdc;border-radius:38px;background:var(--grey-pill);text-align:center;font-size:19px;line-height:26px;color:var(--grey-soft);padding-top:12px}
  .note{left:150px;top:2178px;width:900px;text-align:center;font-size:14.5px;line-height:24px;color:var(--grey-soft)}
  .note strong{color:#333}

  .footer{left:0;top:2287px;width:1200px;height:37px;background:var(--footer);color:var(--white);text-align:center;font-family:"Jost",sans-serif;font-size:12.5px;line-height:37px}
</style>
</head>
<body>

<header class="abs hero" role="img" aria-label="Photo: city skyline with TV tower and river harbour at dusk"></header>
<div class="abs brand">LUKAS RENNER</div>
<nav class="abs nav">
  <a class="active" style="left:0">HOME</a>
  <a style="left:75px">WHAT I DO</a>
  <a style="left:182px">WHY I DO IT &amp; HOW I DO IT</a>
  <a style="left:395px">ABOUT ME</a>
  <a style="left:496px">CONTACT</a>
</nav>
<div class="abs hero-pill">
  <h1 class="hero-title">Sachverständiger für Firmenbewertungen</h1>
  <p class="hero-sub">Sie benötigen ein Gutachten zur Ermittlung des Wertes Ihres Unternehmens</p>
</div>

<div class="abs mini-mark"></div>
<h2 class="abs section-title">WHY YOU SHOULD WORK WITH ME</h2>

<div class="abs reason" style="left:105px">
  <svg width="270" height="137" viewBox="0 0 270 137"><rect x="13" y="13" width="244" height="111" rx="55" fill="none" stroke="var(--grey-mark)" stroke-width="26"/>
    <g fill="none" stroke="#555" stroke-width="4" stroke-linecap="round"><circle cx="150" cy="68" r="24"/><path d="M150 52v16l11 8"/><path d="M92 58h28M98 68h22M104 78h16"/></g></svg>
  <h3>Schnell</h3>
  <p>Sie bekommen Ihr Gutachten zeitnah<br>(innerhalb von max. 21 Tagen nach Zugang<br>aller benötigten Unterlagen)</p>
</div>
<div class="abs reason" style="left:450px">
  <svg width="270" height="137" viewBox="0 0 270 137"><rect x="13" y="13" width="244" height="111" rx="55" fill="none" stroke="var(--grey-mark)" stroke-width="26"/>
    <g fill="none" stroke="#555" stroke-width="4"><rect x="98" y="40" width="74" height="52" rx="3"/><path d="M110 55h50M110 65h50M110 75h30"/><circle cx="160" cy="86" r="7" fill="#fff"/></g></svg>
  <h3>Zertifiziert</h3>
  <p>Sie erhalten ein qualifiziertes und<br>belastbares Gutachten von einem<br>zertifizierten Sachverständigen (höchste<br>Akzeptanz bei allen Parteien)</p>
</div>
<div class="abs reason" style="left:795px">
  <svg width="270" height="137" viewBox="0 0 270 137"><rect x="13" y="13" width="244" height="111" rx="55" fill="none" stroke="var(--grey-mark)" stroke-width="26"/>
    <g fill="#555"><rect x="133" y="45" width="4" height="40"/><rect x="100" y="52" width="70" height="4"/><circle cx="112" cy="46" r="9"/><circle cx="160" cy="42" r="13"/><path d="M118 104l8-22h18l8 22z"/></g></svg>
  <h3>Verständlich</h3>
  <p>Ihr Gutachten wird für Sie logisch<br>und nachvollziehbar sein und kein<br>“Fachchinesisch” enthalten</p>
</div>

<section class="abs promise" role="img" aria-label="Photo: the expert in a white shirt leaning on a railing in a bright concrete interior"></section>
<div class="abs promise-text">
  <h2>MY QUALITY PROMISE :</h2>
  <p>should the advised date for the preparation<br>of the report be exceeded, you will receive<br>the report free of chare (I waive my fee)</p>
</div>

<ul class="abs questions" style="left:120px;top:1856px">
  <li>What are the buying motives of the customers?</li>
  <li>Sie wollen Anteile Ihres Unternehmens oder ihr gesamtes Unternehmen verkaufen?</li>
  <li>Sie müssen im Rahmen einer Trennung/Scheidung jemanden ausbezahlen und benötigen eine Bemessungsgrundlage?</li>
</ul>
<div class="abs divider"></div>
<ul class="abs questions" style="left:660px;top:1856px">
  <li>Was sind die Kaufmotive der Kunden?</li>
  <li>Sie wollen Ihr Unternehmen auf Ihre Erben übertragen und benötigen eine Bewertung für das Finanzamt?</li>
</ul>

<div class="abs cta">Lassen Sie Ihr Unternehmen von einem qualifizerten Sachverständigen bewerten und gehen somit<br>vielen (unnötigen) Streitereien aus dem Weg.</div>
<p class="abs note"><strong>Merke</strong>: Die Kosten für ein Gutachten sind immer überproportional günstiger als die Kosten für Rechtsstreitigkeiten. Und das losgelöst von der psychischen Belastung einer solchen Auseinandersetzung ...</p>

<footer class="abs footer">© 2019 by Lukas Renner. All right reserved.</footer>
</body>
</html>
```